Guiding Resilient Artistry through Calm Emotional Training

FLYER FOR MENTAL SKILLS TRAINING AND CHOREOGRAPHY
For more information please see attachment.
For more information please see attachment
Thank you..

Target Market(s)

athletes, dancers and choreographers

Industry/Entity Type

Training

Font styles to use
Serif

Colors
32a5d7
0392cd
85cae6

Requirements
Must have
• email address: gracebymiralovane@mailnova.net
• phone number: (555) 231-7809
• Facebook: www.pagewave.net/movementbymiralovane
Nice to have
• Everything that is in the file I have attached. Flattering and eye catching unisex color. Logo should be included on the very first page.

```html
<!DOCTYPE html>
<html lang="en">
<head>
<meta charset="utf-8">
<title>GRACE Flyer – Back</title>
<link href="https://fonts.googleapis.com/css2?family=Lato:wght@400;700;900&display=swap" rel="stylesheet">
<style>
  :root {
    --navy: #253f8e;
    --accent: #0392cd;
    --accent-soft: #32a5d7;
    --ink: #1e1e1e;
    --label-grey: #9a9a9a;
    --frame: #a8a8a8;
    --wash-start: #eff0f5;
    --wash-end: #f1f6fa;
    --paper: #ffffff;
  }
  * { margin: 0; padding: 0; box-sizing: border-box; }
  html, body { width: 1200px; height: 1000px; overflow: hidden; background: var(--paper); }
  body { position: relative; font-family: "Lato", Arial, sans-serif; color: var(--ink); }

  .side-label {
    position: absolute; top: 26px; left: 0; width: 1200px; text-align: center;
    font-family: Arial, Helvetica, sans-serif;
    font-weight: 700; font-size: 42px; letter-spacing: 1px; color: var(--label-grey);
  }
  .spread {
    position: absolute; left: 38px; top: 83px; width: 1132px; height: 802px;
    border: 1px solid var(--frame); overflow: hidden;
  }
  .backdrop {
    position: absolute; inset: 0;
    background: linear-gradient(135deg, var(--wash-start) 0%, var(--paper) 50%, var(--wash-end) 100%);
  }
  .fold {
    position: absolute; left: 566px; top: 0; height: 100%;
    border-left: 1px dashed var(--frame);
  }

  .section-bar {
    position: absolute; height: 29px; background: var(--navy); color: #fff;
    font-weight: 700; font-size: 19px; line-height: 29px; padding-left: 38px;
    white-space: nowrap;
  }
  .bullet-list { position: absolute; list-style: none; }
  .bullet-list li { position: relative; font-size: 16px; line-height: 21px; margin-bottom: 21px; }
  .bullet-list li svg.bullet { position: absolute; left: -35px; top: 3px; width: 15px; height: 13px; }
  .bullet-list b { font-weight: 700; }

  .about-list { left: 158px; top: 197px; width: 370px; }
  .benefit-list { left: 158px; top: 658px; width: 420px; }
  .offer-list { left: 723px; top: 205px; width: 410px; }
  .offer-title { color: var(--accent); font-weight: 700; display: block; }
</style>
</head>
<body>
  <svg width="0" height="0" style="position:absolute" aria-hidden="true">
    <defs>
      <symbol id="arrow" viewBox="0 0 15 13">
        <path d="M1 6.5C1 3.6 2.8 2.2 6 2.2H8V0L14.5 6.5 8 13V10.8H6C2.8 10.8 1 9.4 1 6.5Z" fill="#0392cd"/>
      </symbol>
    </defs>
  </svg>

  <div class="side-label">BACK</div>

  <section class="spread">
    <div class="backdrop" role="img" aria-label="Soft pastel decorative backdrop"></div>
    <div class="fold"></div>
  </section>

  <div class="section-bar" style="left:40px;top:143px;width:290px;">MiraLovane Is:</div>
  <ul class="bullet-list about-list">
    <li><svg class="bullet"><use href="#arrow"/></svg>The founder of GRACE</li>
    <li><svg class="bullet"><use href="#arrow"/></svg>A former Gymnast for the Lakeshore State<br>University</li>
    <li><svg class="bullet"><use href="#arrow"/></svg>A Choreographer of Gymnastic Floor and Beam<br>Routines</li>
    <li><svg class="bullet"><use href="#arrow"/></svg>A Graduate of the Lakeshore State University<br>Bachelor of Arts in Liberal Arts and Sciences</li>
    <li><svg class="bullet"><use href="#arrow"/></svg>A Graduate of Harrow University<br>Masters in Counseling with Specialization in<br>Sport and Health</li>
    <li><svg class="bullet"><use href="#arrow"/></svg>A member of Pulse Step Dance Company<br>founded in the Riverbend area</li>
  </ul>

  <div class="section-bar" style="left:40px;top:606px;width:488px;">Why Will You Benefit from Mental Skills Training?</div>
  <ul class="bullet-list benefit-list">
    <li><svg class="bullet"><use href="#arrow"/></svg>Consider all athletic successes that you’ve had. What<br><b>percentage</b> of time were you mentally focused?</li>
    <li><svg class="bullet"><use href="#arrow"/></svg>Consider your athletic performance. What <b>percentage</b><br>of mistakes were considered to be mental errors?</li>
    <li><svg class="bullet"><use href="#arrow"/></svg>Consider your preparation. What <b>percentage</b> of time do<br>you spend on mental training?</li>
  </ul>

  <div class="section-bar" style="left:605px;top:143px;width:343px;padding-left:42px;">What does GRACE have to offer?</div>
  <ul class="bullet-list offer-list">
    <li><svg class="bullet"><use href="#arrow"/></svg><span class="offer-title">Mental Block Interventions</span>Mental block interventions are designed specifically to<br>develop mental toughness required to perform skills<br>otherwise avoided due to fear.</li>
    <li><svg class="bullet"><use href="#arrow"/></svg><span class="offer-title">Imagery Workshops</span>Imagery Utilizes the Powerful Dynamics of the Mind.<br>This technique provides athletes with the proper way to<br>visualize successful performances prior to competition,<br>improving the level of consistent and quality<br>performances.</li>
    <li><svg class="bullet"><use href="#arrow"/></svg><span class="offer-title">Goal Setting Workshops</span>Goal setting is one of the most important mental<br>skill techniques providing guidance, motivation<br>and ultimately increasing performance levels. These<br>workshops will allow athletes to create team long-term<br>goals as well as individual goals.</li>
    <li><svg class="bullet"><use href="#arrow"/></svg><span class="offer-title">Motivation Workshops</span>Motivation is essential to optimal performance for any<br>athlete. These specific workshops provide motivating<br>scripts, personal mantras as well as supportive team<br>slogans.</li>
    <li><svg class="bullet"><use href="#arrow"/></svg><span class="offer-title">Team Cohesion Activities</span>team cohesion is another element required for peak<br>performances. Team cohesion workshops incorporate<br>activities attached to learning objectives that assist in<br>uniting a team in a fun and innovative manner.</li>
  </ul>
</body>
</html>
```